Illustrationen für Unternehmensberatung im Bereich der Vorsorge- und Notfallplanung
ich bin hoch zufrieden mit dem Ergebnis. Vor allem ging alles ganz schnell und unkompliziert. Danke auch an dieser Stelle an Lennart :-)
Zielgruppe
wir beraten kleine und mittelständige Unternehmer/Innen im Bereich der Vorsorge- und Notfallplanung, sowohl im privaten wie im betrieblichen Bereich.
Aufgabenstellung
Die Illustrationen sollten das Niveau von freiberuflich, selbständig Tätigen und von Unternehmern treffen. Nicht zu verspielt, seriös und für eine Zielgruppe ab 35 Jahren geeignet.

```html
<!DOCTYPE html>
<html lang="de">
<head>
<meta charset="utf-8">
<title>Unternehmer-Beratung ganzheitlich definiert</title>
<link rel="stylesheet" href="https://fonts.googleapis.com/css2?family=Open+Sans:wght@300;400;700;800&display=swap">
<style>
  :root {
    --bg-deep: #0a2a44;
    --bg-mid: #14628f;
    --bg-light: #1d7bb0;
    --white: #ffffff;
    --tab-back: #f4f6f8;
    --tab-yellow: #ecc255;
    --tab-orange: #f7931e;
  }
  html, body { margin: 0; padding: 0; overflow: hidden; }
  body { width: 1200px; height: 848px; background: var(--bg-deep); }
  .canvas {
    position: relative; width: 1200px; height: 848px; overflow: hidden;
    font-family: "Open Sans", sans-serif; color: var(--white);
  }
  .backdrop {
    position: absolute; inset: 0;
    background:
      radial-gradient(ellipse 55% 60% at 50% 45%, var(--bg-light) 0%, var(--bg-mid) 45%, transparent 85%),
      linear-gradient(90deg, #0d3a5c 0%, #12557f 30%, #14628f 55%, #0c3453 100%);
  }
  .connectors { position: absolute; inset: 0; }
  .connectors line { stroke: var(--white); stroke-width: 3; stroke-dasharray: 9 8; opacity: .9; }
  .divider { position: absolute; top: 408px; height: 2px; background: var(--white); }
  .divider--left { left: 0; width: 321px; }
  .divider--right { left: 871px; width: 329px; }

  .headline {
    position: absolute; top: 27px; left: 0; width: 1200px; margin: 0;
    text-align: center; font-weight: 300; font-size: 33px; letter-spacing: .2px;
  }
  .headline strong { font-weight: 700; }
  .core {
    position: absolute; top: 369px; left: 0; width: 1200px; margin: 0;
    text-align: center; font-weight: 700; font-size: 26px; line-height: 32px;
  }
  .level {
    position: absolute; left: 500px; width: 260px; margin: 0;
    text-align: center; font-size: 19.5px; line-height: 24px; font-weight: 400;
  }
  .level--private { top: 248px; left: 499px; }
  .level--business { top: 525px; left: 497px; }
  .closing {
    position: absolute; top: 778px; left: 0; width: 1200px; margin: 0;
    text-align: center; font-weight: 700; font-size: 35px;
  }

  .role {
    position: absolute; width: 175px; height: 54px;
  }
  .role--narrow { width: 155px; }
  .role--wide { width: 184px; }
  .role svg { position: absolute; inset: 0; width: 100%; height: 100%; }
  .role__label {
    position: absolute; left: 0; right: 0; bottom: 7px;
    text-align: center; font-weight: 700; font-size: 17px; line-height: 22px;
    white-space: nowrap;
  }
  .role--statement { width: 155px; height: 97px; }
  .role--statement .role__label {
    bottom: 10px; font-weight: 400; font-size: 16.5px; line-height: 20.5px;
  }
  .role--statement .role__label b { font-weight: 700; }
</style>
</head>
<body>
<div class="canvas">
  <div class="backdrop" role="img" aria-label="Unscharfes Foto einer Besprechung von Geschäftsleuten in einem Büro"></div>

  <svg class="connectors" viewBox="0 0 1920 1357" width="1200" height="848" aria-hidden="true">
    <line x1="1006" y1="258" x2="1007" y2="380"/>
    <line x1="1006" y1="492" x2="1007" y2="570"/>
    <line x1="710" y1="292" x2="880" y2="565"/>
    <line x1="482" y1="388" x2="752" y2="575"/>
    <line x1="1285" y1="345" x2="1148" y2="553"/>
    <line x1="1553" y1="386" x2="1333" y2="570"/>
    <line x1="432" y1="550" x2="502" y2="592"/>
    <line x1="1565" y1="578" x2="1425" y2="608"/>
    <line x1="492" y1="738" x2="422" y2="778"/>
    <line x1="694" y1="742" x2="358" y2="937"/>
    <line x1="774" y1="751" x2="441" y2="1045"/>
    <line x1="893" y1="757" x2="710" y2="1045"/>
    <line x1="1005" y1="748" x2="1003" y2="822"/>
    <line x1="1000" y1="930" x2="998" y2="1032"/>
    <line x1="1138" y1="775" x2="1240" y2="1020"/>
    <line x1="1265" y1="748" x2="1485" y2="983"/>
    <line x1="1377" y1="746" x2="1532" y2="846"/>
    <line x1="1407" y1="708" x2="1548" y2="738"/>
  </svg>

  <svg width="0" height="0" style="position:absolute" aria-hidden="true">
    <defs>
      <linearGradient id="tabFill" x1="0" y1="0" x2="1" y2="0">
        <stop offset="0" stop-color="#ecc255"/>
        <stop offset=".55" stop-color="#f1b03f"/>
        <stop offset="1" stop-color="#f7931e"/>
      </linearGradient>
      <symbol id="folder" viewBox="0 0 100 35" preserveAspectRatio="none">
        <path d="M0 2 Q0 0 2 0 H98 Q100 0 100 2 V35 H0 Z" fill="#f4f6f8"/>
        <path d="M0 12 H68 C72 12 72 3.5 76 3.5 H100 V35 H0 Z" fill="url(#tabFill)"/>
      </symbol>
      <symbol id="folderTall" viewBox="0 0 100 62" preserveAspectRatio="none">
        <path d="M0 2 Q0 0 2 0 H98 Q100 0 100 2 V62 H0 Z" fill="#f4f6f8"/>
        <path d="M0 7 H68 C72 7 72 2 76 2 H100 V62 H0 Z" fill="url(#tabFill)"/>
      </symbol>
    </defs>
  </svg>

  <h1 class="headline">Unternehmer-Beratung <strong>ganzheitlich</strong> definiert</h1>

  <p class="level level--private">persönliche /<br>private Ebene</p>
  <div class="divider divider--left"></div>
  <div class="divider divider--right"></div>
  <p class="core">Unternehmen / in - Persönlichkeiten<br>in unterschiedlichen Rollen</p>
  <p class="level level--business">geschäftliche<br>Ebene</p>

  <!-- private roles -->
  <div class="role role--narrow" style="left:546px;top:94px"><svg><use href="#folder"/></svg><span class="role__label">Mensch</span></div>
  <div class="role role--narrow" style="left:361px;top:115px"><svg><use href="#folder"/></svg><span class="role__label">Versorger</span></div>
  <div class="role role--narrow" style="left:726px;top:121px"><svg><use href="#folder"/></svg><span class="role__label">Mutter / Vater</span></div>
  <div class="role role--wide" style="left:155px;top:155px"><svg><use href="#folder"/></svg><span class="role__label">Tochter / Sohn</span></div>
  <div class="role role--wide" style="left:896px;top:172px"><svg><use href="#folder"/></svg><span class="role__label">Ehefrau / -mann</span></div>
  <div class="role role--wide" style="left:79px;top:274px"><svg><use href="#folder"/></svg><span class="role__label">Schwester / Bruder</span></div>
  <div class="role role--wide" style="left:946px;top:297px"><svg><use href="#folder"/></svg><span class="role__label">Freundin / Freund</span></div>

  <!-- business roles -->
  <div class="role" style="left:60px;top:455px"><svg><use href="#folder"/></svg><span class="role__label">Ausbilder</span></div>
  <div class="role" style="left:989px;top:438px"><svg><use href="#folder"/></svg><span class="role__label">Gesellschafter</span></div>
  <div class="role" style="left:968px;top:532px"><svg><use href="#folder"/></svg><span class="role__label">Kaufmann</span></div>
  <div class="role" style="left:36px;top:570px"><svg><use href="#folder"/></svg><span class="role__label">Vorgesetzter</span></div>
  <div class="role" style="left:950px;top:641px"><svg><use href="#folder"/></svg><span class="role__label">Verkäufer</span></div>
  <div class="role" style="left:92px;top:662px"><svg><use href="#folder"/></svg><span class="role__label">Entscheider</span></div>
  <div class="role" style="left:328px;top:674px"><svg><use href="#folder"/></svg><span class="role__label">Entscheider</span></div>
  <div class="role role--statement" style="left:546px;top:670px"><svg><use href="#folderTall"/></svg><span class="role__label"><b>Unternehmer</b> ist<br>das Gegenteil von<br><b>Unterlasser</b></span></div>
  <div class="role" style="left:737px;top:666px"><svg><use href="#folder"/></svg><span class="role__label">Visionär</span></div>

  <p class="closing">Viele Rollen für einen Menschen, oder ?</p>
</div>
</body>
</html>
```